LEARN Business Skills so you can Earn a good living

size of the poster is 8”x 10.75" plus 0.25" bleed.
Please leave 1 inch on the bottoum for footer
I want a design a poster that will attract people's attention.
I appreciate a creative ad however the ad should not take away from being able to clearly read the text.
-I also appreciate a simple creative ad that is not too busy.
-you can use graphics, vectors, or pictures of real people.
-however, if you use real people it should be a white male that is wearing a white shirt and look like a professional person.

Target Market(s)

Potential young business people

Industry/Entity Type

education

Requirements
Must have
• easy to read the text
Nice to have
• I would like a "creative" simple ad that is easy to be read
Should not have
• pictures of women

```html
<!DOCTYPE html>
<html lang="en">
<head>
<meta charset="utf-8">
<title>Learn It to Earn It – Business Enrichment Course</title>
<link rel="stylesheet" href="https://fonts.googleapis.com/css2?family=Playfair+Display:wght@700;800&family=Montserrat:wght@400;500;600;700&family=Allura&display=swap">
<style>
  :root {
    --ink: #2a2d35;
    --paper: #f7f8fa;
    --white: #ffffff;
    --dot-tone: #c9d0d0;
    --photo-light: #f1f1f1;
    --photo-mid: #d9d4ce;
  }
  * { margin: 0; padding: 0; box-sizing: border-box; }
  html, body { width: 939px; height: 1200px; overflow: hidden; background: var(--ink); }
  .poster {
    position: relative;
    width: 939px;
    height: 1200px;
    overflow: hidden;
    background: var(--ink);
    font-family: "Montserrat", Arial, sans-serif;
    color: var(--ink);
  }
  .backdrop { position: absolute; inset: 0; }

  .headline {
    position: absolute;
    left: 0; top: 0;
    width: 100%;
    font-family: "Playfair Display", Georgia, serif;
    font-weight: 800;
    color: var(--white);
    line-height: 1;
  }
  .headline__line {
    position: absolute;
    font-size: 126px;
    letter-spacing: -2px;
    white-space: nowrap;
  }
  .headline__line--learn { left: 148px; top: 72px; }
  .headline__line--earn { left: 245px; top: 205px; }
  .headline__connector {
    position: absolute;
    left: 120px; top: 240px;
    font-family: "Allura", cursive;
    font-weight: 400;
    font-size: 110px;
    color: var(--white);
  }

  .course-title {
    position: absolute;
    left: 85px; top: 392px;
    font-size: 55px;
    font-weight: 600;
    line-height: 66px;
    letter-spacing: 0.5px;
  }
  .course-tagline {
    position: absolute;
    left: 85px; top: 586px;
    font-size: 24px;
    font-weight: 400;
    line-height: 33px;
  }
  .benefits {
    position: absolute;
    left: 85px; top: 665px;
    width: 420px;
  }
  .benefits__heading {
    font-size: 23px;
    font-weight: 700;
    line-height: 28px;
  }
  .benefits__list {
    margin-top: 12px;
    font-size: 21.5px;
    line-height: 27px;
    font-weight: 400;
  }
  .benefits__list strong { font-weight: 700; }

  .topics {
    position: absolute;
    left: 90px; top: 958px;
    width: 300px;
    font-size: 12px;
    line-height: 16.5px;
    font-weight: 500;
    color: var(--white);
  }

  .model-photo {
    position: absolute;
    left: 488px; top: 620px;
    width: 451px; height: 580px;
    border-radius: 180px 120px 0 0;
    background: linear-gradient(180deg, var(--photo-mid) 0%, var(--photo-light) 35%, var(--white) 70%, var(--photo-light) 100%);
  }
</style>
</head>
<body>
<main class="poster">
  <svg class="backdrop" width="939" height="1200" viewBox="0 0 939 1200" aria-hidden="true">
    <defs>
      <linearGradient id="dot-fade" x1="0" y1="0" x2="1" y2="0.6">
        <stop offset="0" stop-color="var(--dot-tone)" stop-opacity="0.55"/>
        <stop offset="0.35" stop-color="var(--dot-tone)" stop-opacity="0"/>
      </linearGradient>
    </defs>
    <polygon class="light-panel" points="0,343 939,438 939,986 0,847" fill="var(--paper)"/>
    <polygon class="light-panel__tone" points="0,343 939,438 939,986 0,847" fill="url(#dot-fade)"/>
    <line class="accent-rule" x1="334" y1="351" x2="939" y2="413" stroke="var(--white)" stroke-width="4"/>
    <line class="accent-rule" x1="0" y1="865" x2="403" y2="926" stroke="var(--white)" stroke-width="4"/>
  </svg>

  <h1 class="headline">
    <span class="headline__line headline__line--learn">LEARN IT</span>
    <span class="headline__connector">to</span>
    <span class="headline__line headline__line--earn">EARN IT</span>
  </h1>

  <h2 class="course-title">Business<br>Enrichment<br>Course</h2>
  <p class="course-tagline">A proven success of helping people<br>in their livelihoods</p>

  <section class="benefits">
    <h3 class="benefits__heading">Business skills<br>that will help you:</h3>
    <p class="benefits__list">Get a quality job - <strong>start/grow your business-Increase your salary</strong></p>
  </section>

  <p class="topics">Business Admiistration – Small Business Management - Finance - Investments - Computers- Accounting - Sales Marketing - Project Manage - Ment Interviewing Skills - Business Law - Negotiation – Public Speaking - Import / Export - Information Technology - Distribution - Marketing - LedgerLite - Real Estate - Health Care-Management - MARKETSTALL</p>

  <div class="model-photo" role="img" aria-label="Photo of a smiling young professional man in a white shirt pointing toward the course text"></div>
</main>
</body>
</html>
```